Your 'not so average' farmers. We are farmers and entrepreneurs trying to connect the great divide.

KTB (Brosmere Holdings Inc) is a family owned farm (in our 3rd generation). We grow vegetables (corn, soy, potatoes, snap beans) but we also invest in and grow businesses. These other businesses can be non-farming related businesses. We are family oriented, environmentally concise, and active in our small community. We need a business card to hand out to our fellow farmers, businesses we would like to partner with and invest in, and community members. So, we need a card with a natural, 'tenders of the land' feel for the farmers but no overly so that we seem centered on farming for the other businesses. We would like it to have our Company info (name, number, email, phone, fax) then Personal info for us five who run the joint (Name, phone, email). So we will order 100 cards for each 5 who work at KTB (500total) that is professional, not boring or hokey, but catching and unique.
Target Market(s)
Farmers, Business Owners, Investors, Community Members
Industry/Entity Type
Farming
Contact Information for Business Card
Office info on one side:
Brosmere Holdings Inc.
1187 Larkin Rd.
Pell Hollow, WI 54872
Office: (608) 555-0417
Fax: (608) 555-0283
brosmereoffice@quillpost.example
Personal Info for the 5 who run KTB. Everybody will have their own personal info on their cards(maybe on the other side):
Name
Mobile
Email
Look and feel

```html
<!DOCTYPE html>
<html lang="en">
<head>
<meta charset="utf-8">
<title>Brosmere Holdings Inc. – Business Cards</title>
<link rel="stylesheet" href="https://fonts.googleapis.com/css2?family=Old+Standard+TT:wght@400;700&display=swap">
<style>
  :root {
    --backdrop: #e9e4dc;
    --card-light: #faf8f4;
    --card-shade: #e6e1d8;
    --band-dark: #3f2f17;
    --band-mid: #56421f;
    --stitch: #b9a36a;
    --name-green: #b8d25a;
    --detail-gold: #e3c98a;
    --mark-green: #8cc43f;
    --shadow: rgba(40, 30, 15, 0.28);
  }
  * { box-sizing: border-box; margin: 0; padding: 0; }
  html, body {
    width: 1200px;
    height: 800px;
    overflow: hidden;
    background: var(--backdrop);
  }
  .canvas {
    width: 1200px;
    height: 800px;
    display: flex;
    align-items: center;
    justify-content: center;
    gap: 48px;
    font-family: "Old Standard TT", Georgia, serif;
  }
  .card {
    position: relative;
    width: 520px;
    height: 298px;
    background: linear-gradient(135deg, var(--card-light) 0%, #f1ede6 55%, var(--card-shade) 100%);
    box-shadow: 0 14px 30px var(--shadow), 0 2px 4px rgba(0,0,0,0.12);
    overflow: hidden;
  }
  .mark {
    position: absolute;
    left: 0;
    right: 0;
    top: 44px;
    display: flex;
    align-items: center;
    justify-content: center;
    gap: 10px;
  }
  .mark-dot {
    width: 14px;
    height: 14px;
    border-radius: 50%;
    background: var(--mark-green);
  }
  .mark-name {
    font-size: 44px;
    font-weight: 700;
    color: var(--mark-green);
    letter-spacing: 2px;
  }
  .band {
    position: absolute;
    left: 0;
    right: 0;
    top: 132px;
    height: 116px;
    background: linear-gradient(180deg, var(--band-mid) 0%, var(--band-dark) 60%, #352711 100%);
    display: flex;
    flex-direction: column;
    align-items: center;
    justify-content: center;
    text-align: center;
  }
  .band::before,
  .band::after {
    content: "";
    position: absolute;
    left: 0;
    right: 0;
    border-top: 1px dashed var(--stitch);
  }
  .band::before { top: 7px; }
  .band::after { bottom: 7px; }
  .company-name,
  .person-name {
    font-variant: small-caps;
    font-weight: 700;
    color: var(--name-green);
    letter-spacing: 1px;
  }
  .company-name { font-size: 22px; margin-bottom: 4px; }
  .person-name { font-size: 24px; margin-bottom: 6px; }
  .detail {
    font-size: 15px;
    line-height: 1.35;
    color: var(--detail-gold);
  }
  .card--personal .detail { font-size: 17px; }
</style>
</head>
<body>
<main class="canvas">
  <article class="card card--personal">
    <div class="mark">
      <span class="mark-dot"></span>
      <span class="mark-name">KTB</span>
    </div>
    <section class="band">
      <h2 class="person-name">Dale Verhoek</h2>
      <p class="detail">Mobile: (608) 555-0192</p>
      <p class="detail">dverhoek@quillpost.example</p>
    </section>
  </article>

  <article class="card card--office">
    <div class="mark">
      <span class="mark-dot"></span>
      <span class="mark-name">KTB</span>
    </div>
    <section class="band">
      <h1 class="company-name">Brosmere Holdings Inc.</h1>
      <p class="detail">1187 Larkin Rd. Pell Hollow, WI 54872</p>
      <p class="detail">Office: (608) 555-0417 Fax: (608) 555-0283</p>
      <p class="detail">brosmereoffice@quillpost.example</p>
    </section>
  </article>
</main>
</body>
</html>
```